Chiropractic front sign

Our current sign is in need of upgrading. Please see attached business cards, to get a "feel" of our current design. We love this design, and would like to see something congruent for the front of our office, yet easily visible.
Also attached is our logo in 2 different formats, as well as a picture of our front office. The sign will be on the main st, to the right viewing area of this picture.
The sign will be carved, on HDU, double sided, and hung facing the people driving by. The dimensions are 48" wide, by 30" in height. that are available for this sign.
I would like at the very least my logo on it, with the word, "chiropractic".
Here is my website for any reference: www.spinewellclinic-example.com
Updates

Project Deadline Extended
Reason: Not content with current designs submitted

Industry/Entity Type

Business

Colors
eb1f27

Requirements
Must have
• logo
• chiropractic
Nice to have
• More than just a rectangle, or oval sign...it will be carved, so something that is unique, helps it stand out on the street.

```html
<!DOCTYPE html>
<html lang="en">
<head>
<meta charset="utf-8">
<title>Spinewell Chiropractic – Front Sign</title>
<link rel="stylesheet" href="https://fonts.googleapis.com/css2?family=Questrial&family=Ultra&display=swap">
<style>
  :root {
    --sign-maroon: #5e0006;
    --sign-white: #ffffff;
    --sign-black: #000000;
    --header-charcoal: #3d3d37;
    --brand-red: #eb1f27;
    --emblem-grey: #7d7d7d;
    --address-chalk: #ececec;
  }
  html, body {
    margin: 0;
    padding: 0;
    width: 1200px;
    height: 955px;
    overflow: hidden;
    background: var(--sign-white);
  }
  .sign {
    display: block;
    width: 1200px;
    height: 955px;
  }
  .sign-frame { fill: var(--sign-maroon); }
  .sign-panel { fill: var(--sign-black); stroke: var(--sign-white); stroke-width: 7; }
  .sign-header { fill: var(--header-charcoal); }
  .brand-name {
    font-family: "Questrial", sans-serif;
    font-size: 118px;
    fill: var(--sign-white);
  }
  .brand-dot { fill: var(--brand-red); }
  .emblem-area { fill: var(--emblem-grey); }
  .service-rule { stroke: var(--sign-white); stroke-width: 3; }
  .service-name {
    font-family: "Questrial", sans-serif;
    font-size: 136px;
    fill: var(--sign-white);
  }
  .street-address {
    font-family: "Ultra", serif;
    font-size: 60px;
    fill: var(--address-chalk);
  }
</style>
</head>
<body>
<svg class="sign" viewBox="0 0 1280 1000" preserveAspectRatio="none" xmlns="http://www.w3.org/2000/svg" aria-label="Spinewell Chiropractic front sign">
  <defs>
    <clipPath id="panel-clip">
      <path d="M 63,248 A 50 62 0 0 0 113,178 L 318,155 Q 640,20 962,155 L 1167,178 A 50 62 0 0 0 1217,248 L 1217,862 A 50 62 0 0 0 1167,922 Q 640,958 113,922 A 50 62 0 0 0 63,862 Z"/>
    </clipPath>
  </defs>

  <path class="sign-frame" d="M 35,225 A 60 75 0 0 0 95,150 L 305,128 Q 640,-5 975,128 L 1185,150 A 60 75 0 0 0 1245,225 L 1245,880 A 60 70 0 0 0 1185,950 Q 640,1000 95,950 A 60 70 0 0 0 35,880 Z"/>

  <path class="sign-panel" d="M 63,248 A 50 62 0 0 0 113,178 L 318,155 Q 640,20 962,155 L 1167,178 A 50 62 0 0 0 1217,248 L 1217,862 A 50 62 0 0 0 1167,922 Q 640,958 113,922 A 50 62 0 0 0 63,862 Z"/>
  <rect class="sign-header" x="60" y="0" width="1160" height="250" clip-path="url(#panel-clip)"/>

  <g class="brand">
    <text class="brand-name" x="610" y="305" text-anchor="middle">spinewell</text>
    <circle class="brand-dot" cx="905" cy="275" r="20"/>
  </g>

  <rect class="emblem-area" x="118" y="487" width="157" height="190" rx="20" role="img" aria-label="Chiropractic emblem of winged staff with serpent and health ribbon"/>

  <g class="service">
    <line class="service-rule" x1="300" y1="505" x2="1143" y2="505"/>
    <text class="service-name" x="300" y="625" textLength="843" lengthAdjust="spacingAndGlyphs">chiropractic</text>
    <line class="service-rule" x1="300" y1="662" x2="660" y2="662"/>
    <line class="service-rule" x1="696" y1="662" x2="1143" y2="662"/>
  </g>

  <text class="street-address" x="632" y="830" text-anchor="middle">214 Main St</text>
</svg>
</body>
</html>
```